snugSEAL - packaging design for plastic zip-lock mechansim

Looking for packaging designs for my patented product, which provides the ability to lock and close existing plastic bags, which have been opened up (like sugar or flour bag, snack bag, etc.). With applying snugSEAL to any bag once opened, the products can be held safe, locked and dry.
Please check my supporting documentation attached, including logos and packaging description.
The packaging design has to make clear to the customer:
- WHAT is this product for
- how to USA
- what are the BENEFITS and the VALUE
I am looking for a long term cooperation with the winning designer, as I will need multiple variations of the packaging depending on individual product usage. I am thinking of approximately 10 different variations in the future.
Updates
Project Deadline Extended Reason: Extending deadline to receive more designs. Please submit your designs according to my description. Let me know if any questions!This will be a long term cooperation as I will need subsequent designs for alternative product variations in the future. Added Saturday, October 22, 2016
Target Market(s)
All consumers who buy products in the supermarket. In particular when they buy products in bags (like salt, sugar, flour, detergents, snacks, ...)
Industry/Entity Type
Retail
Look and feel
Each slider illustrates characteristics of the customer's brand and the style your logo design should communicate.

```html
<!DOCTYPE html>
<html lang="en">
<head>
<meta charset="utf-8">
<title>snugSEAL – Carton Front and Side</title>
<link href="https://fonts.googleapis.com/css2?family=Fira+Sans+Condensed:wght@500;600;700;800&display=swap" rel="stylesheet">
<style>
  :root {
    --navy: #0d2a63;
    --navy-deep: #0a214f;
    --blue-mid: #0a4e9a;
    --blue-glow: #0a86cf;
    --red: #e0201f;
    --red-dark: #b8161a;
    --white: #ffffff;
    --stage: #f1f2f4;
    --bag-light: #f4f5f7;
    --bag-shade: #cfd3d9;
    --stripe: #1e7fd1;
  }
  * { margin: 0; padding: 0; box-sizing: border-box; }
  html, body {
    width: 1126px; height: 1200px; overflow: hidden;
    background: var(--stage);
    font-family: "Fira Sans Condensed", sans-serif;
  }
  .canvas { position: relative; width: 1126px; height: 1200px; }

  .panel { position: absolute; top: 40px; height: 1120px; overflow: hidden; background: var(--navy); }
  .panel-art { position: absolute; inset: 0; }
  .front-panel { left: 113px; width: 640px; }
  .side-panel { left: 753px; width: 260px; }

  /* Front */
  .brand-name {
    position: absolute; left: 0; right: 0; top: 160px;
    text-align: center; color: var(--white);
    font-weight: 800; font-size: 96px; line-height: 1;
  }
  .headline {
    position: absolute; left: 40px; right: 40px; top: 350px;
    text-align: center; color: var(--white);
    font-weight: 600; font-size: 38px; line-height: 1.2;
  }
  .bag-visual {
    position: absolute; left: 170px; top: 470px;
    width: 260px; height: 380px; border-radius: 8px;
    background: linear-gradient(180deg, var(--bag-light) 0%, #e4e7eb 55%, var(--bag-shade) 100%);
  }
  .bag-visual::after {
    content: ""; position: absolute; left: 0; right: -20px; top: 130px;
    height: 8px; background: var(--stripe);
  }
  .stick-hint { position: absolute; left: 440px; top: 560px; width: 70px; height: 150px; }
  .stick-label {
    position: absolute; left: 500px; top: 600px; white-space: nowrap;
    color: var(--white); font-weight: 500; font-size: 22px; line-height: 1.35;
  }
  .benefits {
    position: absolute; left: 24px; top: 868px;
    color: var(--white); font-weight: 500; font-size: 25px; line-height: 1.3;
  }
  .usage {
    position: absolute; left: 24px; top: 1010px; width: 330px;
    color: var(--white); font-weight: 500; font-size: 20px; line-height: 1.25;
    transform: rotate(4deg); transform-origin: left top;
  }
  .count-badge {
    position: absolute; left: 505px; top: 955px;
    width: 110px; height: 110px; background: var(--navy);
    border: 2px solid var(--white);
    color: var(--white); text-align: center;
  }
  .count-number { display: block; font-weight: 700; font-size: 60px; line-height: 1; margin-top: 6px; }
  .count-unit { display: block; font-weight: 600; font-size: 30px; line-height: 1; }
  .length-note {
    position: absolute; left: 505px; top: 1072px; width: 110px;
    text-align: center; color: var(--white); font-weight: 500; font-size: 17px;
  }

  /* Side */
  .side-bag {
    position: absolute; left: 30px; top: 40px; width: 200px; height: 180px; border-radius: 6px;
    background: linear-gradient(160deg, var(--bag-light) 0%, #dfe3e8 60%, var(--bag-shade) 100%);
  }
  .side-bag::after {
    content: ""; position: absolute; left: 0; right: 0; top: 70px; height: 7px; background: var(--navy);
  }
  .rotated { position: absolute; transform: rotate(-90deg); color: var(--white); text-align: center; }
  .side-brand-banner {
    position: absolute; left: 20px; top: 410px; width: 72px; height: 320px; background: var(--red);
  }
  .side-brand {
    left: -105px; top: 536px; width: 320px; height: 68px;
    font-weight: 800; font-size: 46px; line-height: 68px;
  }
  .side-tagline {
    left: -75px; top: 530px; width: 480px; height: 72px;
    font-weight: 600; font-size: 25px; line-height: 1.2;
  }
  .side-count {
    left: 5px; top: 925px; width: 160px; height: 100px;
    border: 2px solid var(--white); background: var(--navy);
    display: flex; align-items: center; justify-content: center; gap: 10px;
  }
  .side-count .count-number { font-size: 70px; margin-top: 0; }
  .side-count .count-unit { font-size: 36px; }
  .side-length {
    left: 130px; top: 960px; width: 160px; height: 30px;
    font-weight: 500; font-size: 20px; line-height: 30px;
  }
</style>
</head>
<body>
<div class="canvas">
  <section class="panel front-panel">
    <svg class="panel-art" viewBox="0 0 640 1120" width="640" height="1120" aria-hidden="true">
      <defs>
        <radialGradient id="front-glow" cx="0.5" cy="0.5" r="0.6">
          <stop offset="0" stop-color="var(--blue-glow)"/>
          <stop offset="0.55" stop-color="var(--blue-mid)"/>
          <stop offset="1" stop-color="var(--navy-deep)"/>
        </radialGradient>
      </defs>
      <rect width="640" height="1120" fill="var(--navy)"/>
      <rect y="270" width="640" height="760" fill="url(#front-glow)"/>
      <path d="M0 125 L640 138 L640 340 Q320 210 0 285 Z" fill="var(--red)"/>
      <path d="M0 285 Q320 210 640 340" fill="none" stroke="var(--white)" stroke-width="4"/>
      <path d="M0 995 Q310 975 640 940 L640 1120 L0 1120 Z" fill="var(--red)"/>
      <path d="M0 995 Q310 975 640 940" fill="none" stroke="var(--white)" stroke-width="4"/>
    </svg>

    <div class="brand-name">snugSEAL</div>
    <h1 class="headline">Transform any Plastic Bag into a<br>ZIPPER Bag!</h1>

    <div class="bag-visual" role="img" aria-label="Clear plastic bag with a snugSEAL zipper strip applied across its top"></div>

    <svg class="stick-hint" viewBox="0 0 70 150" aria-hidden="true">
      <line x1="35" y1="5" x2="35" y2="55" stroke="var(--white)" stroke-width="3"/>
      <polygon points="27,50 43,50 35,66" fill="var(--white)"/>
      <line x1="35" y1="145" x2="35" y2="95" stroke="var(--white)" stroke-width="3"/>
      <polygon points="27,100 43,100 35,84" fill="var(--white)"/>
      <line x1="5" y1="75" x2="65" y2="75" stroke="var(--white)" stroke-width="2" stroke-dasharray="8 6"/>
    </svg>
    <p class="stick-label">Stick on the<br>Plastic Bag</p>

    <p class="benefits">Keeps it Safe,<br>Keeps it Dry<br>Keeps it Locked!</p>

    <p class="usage">Commonly applied on sugar bag,<br>flour bag, snack bag</p>

    <div class="count-badge">
      <span class="count-number">50</span>
      <span class="count-unit">BAGS</span>
    </div>
    <p class="length-note">25 cm length</p>
  </section>

  <section class="panel side-panel">
    <svg class="panel-art" viewBox="0 0 260 1120" width="260" height="1120" aria-hidden="true">
      <defs>
        <radialGradient id="side-glow" cx="0.5" cy="0.5" r="0.7">
          <stop offset="0" stop-color="var(--blue-glow)"/>
          <stop offset="0.55" stop-color="var(--blue-mid)"/>
          <stop offset="1" stop-color="var(--navy-deep)"/>
        </radialGradient>
      </defs>
      <rect width="260" height="1120" fill="var(--navy)"/>
      <rect y="260" width="260" height="560" fill="url(#side-glow)"/>
      <path d="M0 850 L260 790 L260 1120 L0 1120 Z" fill="var(--red)"/>
      <path d="M0 850 L260 790" stroke="var(--white)" stroke-width="4"/>
    </svg>

    <div class="side-bag" role="img" aria-label="Plastic bag sealed with a snugSEAL strip"></div>

    <div class="side-brand-banner"></div>
    <p class="rotated side-brand">snugSEAL</p>
    <p class="rotated side-tagline">Transform any Plastic Bag into a<br>ZIPPER Bag!</p>

    <div class="rotated side-count">
      <span class="count-number">50</span>
      <span class="count-unit">BAGS</span>
    </div>
    <p class="rotated side-length">25 cm length</p>
  </section>
</div>
</body>
</html>
```